Vegan Alfredo Sauce Label Design for Brambleway Pantry Co

We are a food co. committed to making vegan food more accessible to people who want to eat healthier. Our first line of product is vegan Alfredo sauce.
We have 3 flavors:
- Garlic
- Pesto
- Lemony Artichoke
The current project is the design for the first flavor: garlic. However, we would like a template that would translate well to other flavors, so they look like a family of products.
These will be in standard 16 oz jars. The whole label will be approx 6cm x 24cm, but the front visual space is approx 6cm x 10cm. The rest will be nutritional labeling and copy about the company.
We also need a stamp or font- based logo that says Brambleway Pantry Co. (or lower case: brambleway pantry co.), the name of the company.
The picture (attached) of Plantbased Nacho Dip is the closest to what we are going for. Because the sauce is creamy white, a colorful background with off-white font will be best.
We currently have a website, although we are doing a brand over-haul (hence, this posting) www.bramblewaypantryco.example. If the designer is a good fit, we have several more projects, in line.
Other brands we love: Tidewell Grocers, Marlow Ridge Provisions, Pulp Poured Daily.
The final brand should communicate hip, natural and health.
And personally, I love design that is clever and somehow makes me smile.
Target Market(s)
Vegans, vegetarians, and people with common food allergies - all ages.
Young, hip families.
Industry/Entity Type
It Company
Requirements
Must have
- Copy:
Vegan Alfredo or Vegan Alfredo Sauce
Garlic
Brambleway Pantry or Brambleway Pantry Co
16 oz
Nice to have
- May include copy:
Gluten-Free Soy-Free Nut-Free
Should not have
- Neon colors

```html
<!DOCTYPE html>
<html lang="en">
<head>
<meta charset="utf-8">
<title>Vegan Alfredo Garlic Label – Brambleway Pantry Co.</title>
<link rel="stylesheet" href="https://fonts.googleapis.com/css2?family=Yellowtail&family=Arimo:ital,wght@0,400;0,700;1,400;1,700&family=Roboto+Condensed:wght@400;700&display=swap">
<style>
  :root {
    --cream: #f3f5e1;
    --cream-light: #fbfcf4;
    --band-green: #d3e49b;
    --band-green-soft: #dde9ad;
    --pale-yellow: #eef0a6;
    --leaf-green: #b9d86b;
    --forest-green: #4a7a37;
    --forest-deep: #3d6a2e;
    --script-green: #1d7a31;
    --text-green: #3f7a2c;
    --ink: #333333;
    --garlic-light: #f2ecdc;
    --garlic-mid: #d9cfae;
    --logo-yellow: #eee49a;
  }
  html, body {
    margin: 0;
    padding: 0;
    overflow: hidden;
    background: #ffffff;
  }
  .label {
    position: relative;
    width: 1200px;
    height: 713px;
    overflow: hidden;
    background: linear-gradient(to bottom, var(--cream) 0%, var(--cream) 55%, var(--cream-light) 80%, #ffffff 100%);
    font-family: "Arimo", Arial, sans-serif;
  }
  .band-main {
    position: absolute;
    left: 0; top: 203px;
    width: 1052px; height: 30px;
    background: var(--band-green);
  }
  .band-thin {
    position: absolute;
    left: 735px; top: 180px;
    width: 465px; height: 11px;
    background: var(--band-green-soft);
  }
  .stripes {
    position: absolute;
    top: 0; right: 0;
    width: 150px; height: 713px;
    display: flex;
  }
  .stripe-yellow { width: 12px; background: var(--pale-yellow); }
  .stripe-leaf { width: 52px; background: var(--leaf-green); }
  .stripe-forest { width: 76px; background: var(--forest-green); }
  .stripe-deep { width: 10px; background: var(--forest-deep); }

  .brand-mark {
    position: absolute;
    left: 870px; top: 116px;
    display: flex;
    align-items: center;
    gap: 8px;
  }
  .brand-mark .dot {
    width: 14px; height: 14px;
    background: var(--logo-yellow);
  }
  .brand-mark .name {
    font-weight: 700;
    font-size: 17px;
    line-height: 19px;
    color: var(--text-green);
    width: 125px;
  }

  .hero-art {
    position: absolute;
    left: 265px; top: 75px;
    width: 590px; height: 430px;
    border-radius: 46% 48% 40% 42%;
    background: radial-gradient(ellipse at 48% 45%, var(--garlic-light) 0%, var(--garlic-mid) 55%, rgba(217,207,174,0.35) 80%, rgba(243,245,225,0) 100%);
  }

  .title {
    position: absolute;
    margin: 0;
    font-family: "Yellowtail", "Brush Script MT", cursive;
    font-weight: 400;
    color: var(--script-green);
    text-shadow: 1px 1px 0 #e9e2a0, 4px 8px 10px rgba(90,90,70,0.25);
    line-height: 1;
    white-space: nowrap;
    transform-origin: left bottom;
    transform: rotate(-14deg);
  }
  .title-vegan {
    left: 240px; top: 360px;
    font-size: 132px;
  }
  .title-alfredo {
    left: 470px; top: 440px;
    font-size: 140px;
  }

  .flavor-line {
    position: absolute;
    left: 648px; top: 550px;
    font-style: italic;
    font-size: 27px;
    line-height: 30px;
    color: var(--ink);
    margin: 0;
    white-space: nowrap;
  }
  .allergen-line {
    position: absolute;
    left: 707px; top: 599px;
    font-family: "Roboto Condensed", "Arial Narrow", sans-serif;
    font-size: 15px;
    line-height: 16px;
    color: var(--ink);
    margin: 0;
    white-space: nowrap;
  }

  .allergen-note {
    position: absolute;
    left: 58px; top: 398px;
    margin: 0;
    color: var(--text-green);
    font-family: "Roboto Condensed", "Arial Narrow", sans-serif;
    font-size: 15px;
    line-height: 20px;
    font-weight: 700;
    letter-spacing: 0.5px;
  }

  .net-weight {
    position: absolute;
    left: 68px; top: 505px;
    color: var(--text-green);
  }
  .net-weight .amount {
    font-family: "Roboto Condensed", "Arial Narrow", sans-serif;
    font-weight: 700;
    font-size: 72px;
    letter-spacing: -5px;
    line-height: 70px;
  }
  .net-weight .amount small {
    font-size: 36px;
    letter-spacing: 0;
  }
  .net-weight .maker {
    font-style: italic;
    font-weight: 700;
    font-size: 13px;
    margin-top: 6px;
    white-space: nowrap;
  }
</style>
</head>
<body>
  <main class="label">
    <div class="band-main"></div>
    <div class="band-thin"></div>
    <div class="stripes" aria-hidden="true">
      <div class="stripe-yellow"></div>
      <div class="stripe-leaf"></div>
      <div class="stripe-forest"></div>
      <div class="stripe-deep"></div>
    </div>

    <div class="brand-mark">
      <span class="dot"></span>
      <span class="name">Brambleway Pantry Co.</span>
    </div>

    <div class="hero-art" role="img" aria-label="Painted illustration of a garlic bulb with loose cloves and curling green shoots"></div>

    <h1 class="title title-vegan">Vegan</h1>
    <h1 class="title title-alfredo">Alfredo</h1>

    <p class="flavor-line">Vegan Alfredo sauce Garlic.</p>
    <p class="allergen-line">GLUTEN-FREE SOY-FREE NUT-FREE</p>

    <p class="allergen-note">Gluten free<br>Soy free<br>Nut free</p>

    <div class="net-weight">
      <div class="amount">16<small>oz.</small></div>
      <div class="maker">Brambleway Pantry Co.</div>
    </div>
  </main>
</body>
</html>
```